" Empresa privada voltada a prestação de serviços nos ramos do direito Administrativo, Previdenciário, Tributário e Municipal, para particulares e pessoas jurídicas de direito público. "

```html
<!DOCTYPE html>
<html lang="pt-BR">
<head>
<meta charset="UTF-8">
<title>Papel timbrado – Teixeira Lemos Advocacia</title>
<link href="https://fonts.googleapis.com/css2?family=Cormorant+Garamond:wght@400;500&family=Lato:wght@400&display=swap" rel="stylesheet">
<style>
  :root {
    --backdrop: #ececea;
    --paper: #ffffff;
    --band: #8c8c8c;
    --band-text: #f4f4f4;
    --rule: #d6d6d6;
    --watermark: #f1f1f3;
  }
  html, body {
    margin: 0;
    padding: 0;
    width: 1200px;
    height: 1200px;
    overflow: hidden;
    background: var(--backdrop);
  }
  .letterhead {
    position: absolute;
    left: 311px;
    top: 50px;
    width: 778px;
    height: 1100px;
    background: var(--paper);
    box-shadow: 0 2px 10px rgba(0,0,0,0.08);
    overflow: hidden;
  }
  .watermark {
    position: absolute;
    left: 0;
    right: 0;
    top: 300px;
    text-align: center;
    font-family: "Cormorant Garamond", serif;
    font-weight: 400;
    font-size: 120px;
    line-height: 1;
    color: var(--watermark);
    letter-spacing: 6px;
  }
  .footer-band {
    position: absolute;
    left: 0;
    right: 0;
    bottom: 0;
    height: 250px;
    background: var(--band);
    color: var(--band-text);
  }
  .contact {
    position: absolute;
    left: 44px;
    top: 30px;
    font-family: "Lato", sans-serif;
    font-size: 11px;
    line-height: 1.9;
    letter-spacing: 0.3px;
  }
  .contact .label {
    margin-bottom: 22px;
    text-transform: uppercase;
    letter-spacing: 1.5px;
  }
  .band-rule {
    position: absolute;
    left: 44px;
    right: 44px;
    top: 182px;
    height: 1px;
    background: var(--rule);
  }
  .firm-name {
    position: absolute;
    right: 44px;
    top: 138px;
    font-family: "Cormorant Garamond", serif;
    font-weight: 500;
    font-size: 17px;
    letter-spacing: 3px;
    text-transform: uppercase;
    color: var(--band-text);
    white-space: nowrap;
  }
</style>
</head>
<body>
  <main class="letterhead">
    <div class="watermark" aria-hidden="true">TL</div>
    <footer class="footer-band">
      <address class="contact">
        <div class="label">Escritório</div>
        <div>Rua das Acácias, 120 – Centro</div>
        <div>Cidade Nova – SP, 01234-000</div>
        <div>(11) 4000-1234</div>
        <div>contato@teixeiralemos.adv.br</div>
      </address>
      <div class="firm-name">Teixeira Lemos Advocacia</div>
      <div class="band-rule"></div>
    </footer>
  </main>
</body>
</html>
```